Formal expert report - construction legal and quantum matters

Formal expert report document.

Require a template which includes a front page, content page.

Front page should have logo, some construction pictures (attached).

Remaining pages should have logo and header/footer.

Styles should be set up also.

Letterhead attached for branding colours etc.

Target Market(s)

lawyers, tribunal, arbitrators, fellow experts.

Industry/Entity Type

Construction, legal, quantity surveying, expert

Font styles to use
Other font styles liked:
• Garamond writing style, (will consider a more readable smart modern/professional format)

Colors
0054AA
0677BA
7BADD7
CADEEF
E8F1F8

```html
<!DOCTYPE html>
<html lang="en">
<head>
<meta charset="utf-8">
<title>Kelvra – Formal Expert Report Template</title>
<link rel="stylesheet" href="https://fonts.googleapis.com/css2?family=EB+Garamond:wght@400;500;600&display=swap">
<style>
  :root{
    --slate:#424d5c;
    --brand-blue:#0054aa;
    --rule-blue:#2a5aa8;
    --sky-blue:#8fabd4;
    --pale-blue:#cadeef;
    --mist:#e8f1f8;
    --paper:#ffffff;
    --ink:#3a3f47;
    --backdrop:#cfcfcf;
  }
  *{margin:0;padding:0;box-sizing:border-box}
  html,body{width:968px;height:1200px;overflow:hidden;background:var(--backdrop)}
  body{position:relative;font-family:"EB Garamond",Garamond,serif;color:var(--ink)}
  .page{position:absolute;width:403px;height:521px;background:var(--paper);overflow:hidden;box-shadow:0 6px 10px rgba(0,0,0,.22)}
  .page svg.shapes{position:absolute;left:0;top:0;width:403px;height:521px}
  .abs{position:absolute}

  /* Cover */
  .cover{left:62px;top:53px}
  .cover .hero{left:0;top:0;width:403px;height:300px;
    background:linear-gradient(180deg,#b89a8c 0%,#c7b3ac 22%,#c8cfdc 45%,#e5ebf3 75%,#ffffff 100%)}
  .brand-name{font-weight:400;letter-spacing:.12em;text-align:center;width:100%}
  .cover .brand-name{top:283px;font-size:40px;color:var(--brand-blue);line-height:1}
  .cover .title{top:378px;width:100%;text-align:center;color:#fff;font-size:31px;line-height:35px;letter-spacing:.01em}
  .cover .site{top:470px;width:100%;text-align:center;color:#fff;font-size:7px;letter-spacing:.55em}

  /* Contents */
  .contents{left:485px;top:53px}
  .contents .sky{left:0;top:310px;width:403px;height:211px;
    background:linear-gradient(180deg,#ffffff 0%,#e6ecf4 35%,#c9d6e8 100%)}
  .contents h2{left:35px;top:27px;font-weight:400;font-size:14px;letter-spacing:.02em;color:#4b5463}
  .contents .head-rule{left:58px;top:45px;width:287px;height:1.5px;background:var(--rule-blue)}
  .toc-item{left:58px;width:287px;height:22px;display:flex;align-items:center}
  .toc-num{width:22px;height:22px;border-radius:50%;background:var(--slate);color:#fff;font-size:11px;display:flex;align-items:center;justify-content:center;flex:none}
  .toc-label{font-size:10px;margin-left:11px;white-space:nowrap;color:#2f343b}
  .toc-rule{flex:1;height:1.5px;background:var(--rule-blue);margin-left:5px}

  /* Services */
  .services{left:62px;top:608px}
  .services .page-title{left:31px;top:20px;color:#fff;font-weight:600;font-size:14px;letter-spacing:.02em}
  .services .brand-name{left:auto;right:24px;top:10px;width:auto;font-size:17px;color:#fff}
  .services h3{left:45px;top:80px;width:300px;font-weight:400;font-size:13px;line-height:16px;color:#4b5463}
  .services .h-rule{left:45px;top:119px;width:287px;height:1.5px;background:var(--rule-blue)}
  .services .intro{left:45px;top:132px;width:320px;font-size:6.6px;line-height:9px;color:#2f343b}
  .services .tab{left:0;top:190px;width:236px;height:22px;background:var(--slate);border-radius:0 12px 12px 0;color:#fff;font-weight:600;font-size:13px;padding-left:45px;line-height:22px}
  .services ul{left:45px;top:219px;list-style:none}
  .services li{font-size:7px;line-height:11px;display:flex;align-items:center;color:#2f343b}
  .services li svg{width:5px;height:5px;margin-right:9px}
  .services .meeting{left:45px;top:309px;width:262px;height:174px;
    background:linear-gradient(135deg,#d9d4cd 0%,#8a9bb8 45%,#3e4a63 70%,#b8a98e 100%)}
  .services .footer-text{left:20px;top:505px;font-size:6.5px;color:#fff}
  .services .page-no{left:370px;top:496px;width:8px;height:8px;border-radius:50%;background:var(--slate);color:#fff;font-size:5px;text-align:center;line-height:8px}

  /* Back cover */
  .back{left:495px;top:608px}
  .back .sky{left:0;top:0;width:403px;height:300px;
    background:radial-gradient(ellipse 120px 60px at 205px 270px,#e8d98a 0%,rgba(200,190,130,.6) 45%,rgba(150,160,150,0) 100%),
               linear-gradient(180deg,#8f9a98 0%,#a9b2a6 40%,#9ea79b 70%,#7c8580 100%)}
  .back .brand-name{top:330px;font-size:38px;color:#fff;line-height:1}
  .contact{width:100%;text-align:center;color:#e6e9ee;font-size:6.5px}
  .contact-icon{left:197px;width:9px;height:9px;border-radius:50%;background:#3a5f95}
</style>
</head>
<body>

<!-- Front cover -->
<section class="page cover">
  <div class="abs hero" role="img" aria-label="Construction photo: hand drafting with pencil and scale ruler over plans, city towers overlaid"></div>
  <svg class="shapes" viewBox="0 0 403 521" aria-hidden="true">
    <polygon points="0,276 201,340 403,276 403,316 201,353 0,316" fill="var(--sky-blue)"/>
    <polygon points="0,326 201,362 403,326 403,521 0,521" fill="var(--slate)"/>
  </svg>
  <div class="abs brand-name">KELVRA</div>
  <h1 class="abs title" style="font-weight:400">FORMAL<br>EXPERT REPORT</h1>
  <div class="abs site">WWW.KELVRA.CO.UK</div>
</section>

<!-- Contents page -->
<section class="page contents">
  <div class="abs sky" role="img" aria-label="Photo of tower cranes against a pale sky"></div>
  <h2 class="abs">CONTENT PAGE</h2>
  <div class="abs head-rule"></div>
  <div class="abs toc-item" style="top:87px"><span class="toc-num">1</span><span class="toc-label">Dispute Resolution Services</span><span class="toc-rule"></span></div>
  <div class="abs toc-item" style="top:124px"><span class="toc-num">2</span><span class="toc-label">Planning &amp; Programming</span><span class="toc-rule" style="margin-left:8px"></span></div>
  <div class="abs toc-item" style="top:161px"><span class="toc-num">3</span><span class="toc-label">Expert Services</span><span class="toc-rule" style="margin-left:10px"></span></div>
  <div class="abs toc-item" style="top:197px"><span class="toc-num">4</span><span class="toc-label">Quantity Surveying Services</span><span class="toc-rule"></span></div>
  <div class="abs toc-item" style="top:235px"><span class="toc-num">5</span><span class="toc-label">Contract Services</span><span class="toc-rule" style="margin-left:10px"></span></div>
</section>

<!-- Services page -->
<section class="page services">
  <svg class="shapes" viewBox="0 0 403 521" aria-hidden="true">
    <polygon points="0,0 403,0 403,64 201,28 0,64" fill="var(--slate)"/>
    <path d="M0,498 H92 Q99,498 102,503 H403 V521 H0 Z" fill="var(--slate)"/>
  </svg>
  <div class="abs page-title">SERVICES</div>
  <div class="abs brand-name">KELVRA</div>
  <h3 class="abs">Our Expert Construction Management &amp; Dispute Resolution Services</h3>
  <div class="abs h-rule"></div>
  <p class="abs intro">We have worked across many different industries so nothing is too big or too small. We like to first understand our clients needs whether in construction development, contracting management, quantity surveying or disputes so we can then deliver the best possible service saving money, time and stress.</p>
  <div class="abs tab">Dispute Resolution Services</div>
  <ul class="abs">
    <li><svg viewBox="0 0 10 10"><circle cx="5" cy="5" r="5" fill="var(--slate)"/><path d="M2.6 5.2 4.3 6.8 7.4 3.5" stroke="#fff" stroke-width="1.4" fill="none"/></svg>Dispute Avoidance</li>
    <li><svg viewBox="0 0 10 10"><circle cx="5" cy="5" r="5" fill="var(--slate)"/><path d="M2.6 5.2 4.3 6.8 7.4 3.5" stroke="#fff" stroke-width="1.4" fill="none"/></svg>Dispute Resolution</li>
    <li><svg viewBox="0 0 10 10"><circle cx="5" cy="5" r="5" fill="var(--slate)"/><path d="M2.6 5.2 4.3 6.8 7.4 3.5" stroke="#fff" stroke-width="1.4" fill="none"/></svg>Mediation</li>
    <li><svg viewBox="0 0 10 10"><circle cx="5" cy="5" r="5" fill="var(--slate)"/><path d="M2.6 5.2 4.3 6.8 7.4 3.5" stroke="#fff" stroke-width="1.4" fill="none"/></svg>Negotiation</li>
    <li><svg viewBox="0 0 10 10"><circle cx="5" cy="5" r="5" fill="var(--slate)"/><path d="M2.6 5.2 4.3 6.8 7.4 3.5" stroke="#fff" stroke-width="1.4" fill="none"/></svg>Adjudication Referral</li>
    <li><svg viewBox="0 0 10 10"><circle cx="5" cy="5" r="5" fill="var(--slate)"/><path d="M2.6 5.2 4.3 6.8 7.4 3.5" stroke="#fff" stroke-width="1.4" fill="none"/></svg>Adjudication Defence</li>
    <li><svg viewBox="0 0 10 10"><circle cx="5" cy="5" r="5" fill="var(--slate)"/><path d="M2.6 5.2 4.3 6.8 7.4 3.5" stroke="#fff" stroke-width="1.4" fill="none"/></svg>Settlement Agreements</li>
  </ul>
  <div class="abs meeting" role="img" aria-label="Photo of a business handshake over a desk with laptop and documents"></div>
  <div class="abs footer-text">www.kelvra.co.uk</div>
  <div class="abs page-no">1</div>
</section>

<!-- Back cover -->
<section class="page back">
  <div class="abs sky" role="img" aria-label="Photo of tower cranes silhouetted against a cloudy sunset sky"></div>
  <svg class="shapes" viewBox="0 0 403 521" aria-hidden="true">
    <polygon points="0,229 201,293 403,229 403,273 201,304 0,273" fill="var(--brand-blue)"/>
    <polygon points="0,279 201,312 403,279 403,521 0,521" fill="var(--slate)"/>
  </svg>
  <div class="abs brand-name">KELVRA</div>
  <div class="abs contact-icon" style="top:397px"></div>
  <div class="abs contact" style="top:411px">2nd Floor &nbsp;|&nbsp; 18 Harlow Crescent &nbsp;|&nbsp; Glasgow &nbsp;|&nbsp; G3 7QT</div>
  <div class="abs contact-icon" style="top:426px"></div>
  <div class="abs contact" style="top:439px">07700 900 415</div>
  <div class="abs contact-icon" style="top:454px"></div>
  <div class="abs contact" style="top:465px">hello@kelvra.co.uk</div>
  <div class="abs contact-icon" style="top:479px"></div>
  <div class="abs contact" style="top:491px">www.kelvra.co.uk</div>
</section>

</body>
</html>
```